Kindle Grove Wording For Logo & Business card

I have the logo, I just need the "kindle Grove" wording to go with it, and a business card design. The only thing on the business card is the website info. We provide nature connection experiences, and bolster these efforts through writing and host a platform for community around it.

I also have an idea of what it could look like (sketch), though I'm really not sure how it would come out. I am open to the best design and happy to consider original artwork. You can see what the site is about at KindleGrove.com.

Contact Information for Business Card

The only thing on the business card is the website info and the design. I will put other messaging on the back.

Website lettering (KindleGrove.com) in Montserrat

Logo Text

Kindle Grove (letters optional)

Font styles to use
Other font styles liked:
• montserrat

```html
<!DOCTYPE html>
<html lang="en">
<head>
<meta charset="utf-8">
<title>Kindle Grove – Business Card</title>
<link rel="stylesheet" href="https://fonts.googleapis.com/css2?family=Montserrat:wght@400;500;700;800&display=swap">
<style>
  :root {
    --stage: #2e2a28;
    --purple: #47295f;
    --purple-deep: #3a1f50;
    --orange: #f7801f;
    --orange-deep: #e8541a;
    --white: #ffffff;
    --paper: #fbfbfb;
  }
  * { box-sizing: border-box; margin: 0; padding: 0; }
  html, body { width: 1200px; height: 716px; overflow: hidden; }
  body {
    background: var(--stage);
    font-family: "Montserrat", sans-serif;
    position: relative;
  }
  .card {
    position: absolute;
    top: 208px;
    width: 520px;
    height: 300px;
    overflow: hidden;
    box-shadow: 0 10px 30px rgba(0,0,0,.45);
  }

  /* Front */
  .card-front {
    left: 50px;
    background: var(--purple);
    border-bottom: 6px solid var(--orange);
  }
  .front-brand {
    position: absolute;
    left: 70px;
    top: 100px;
    display: flex;
    align-items: center;
    gap: 22px;
  }
  .brand-dot {
    width: 92px;
    height: 92px;
    border-radius: 50%;
    background: var(--purple-deep);
    border: 3px solid var(--orange);
    flex: none;
  }
  .front-name {
    color: var(--white);
    font-weight: 800;
    font-size: 36px;
    line-height: 1.05;
    letter-spacing: 1px;
    text-transform: uppercase;
  }

  /* Back */
  .card-back {
    left: 630px;
    background: var(--paper);
  }
  .back-shape { position: absolute; inset: 0; }
  .website {
    position: absolute;
    left: 40px;
    top: 140px;
    display: flex;
    align-items: center;
    gap: 8px;
    color: var(--white);
    font-weight: 500;
    font-size: 15px;
  }
  .website svg { width: 13px; height: 13px; fill: var(--orange); flex: none; }
  .back-name {
    position: absolute;
    right: 40px;
    top: 150px;
    color: var(--purple);
    font-weight: 800;
    font-size: 30px;
    line-height: 1.05;
    letter-spacing: 1px;
    text-transform: uppercase;
  }
</style>
</head>
<body>

  <section class="card card-front" aria-label="Business card front">
    <div class="front-brand">
      <span class="brand-dot" aria-hidden="true"></span>
      <p class="front-name">Kindle<br>Grove</p>
    </div>
  </section>

  <section class="card card-back" aria-label="Business card back">
    <svg class="back-shape" viewBox="0 0 520 300" aria-hidden="true">
      <circle cx="70" cy="116" r="244" fill="var(--orange-deep)"/>
      <circle cx="64" cy="112" r="241" fill="var(--orange)"/>
      <circle cx="56" cy="108" r="236" fill="var(--purple)"/>
    </svg>

    <p class="website">
      <svg viewBox="0 0 24 24" aria-hidden="true"><circle cx="12" cy="12" r="10"/></svg>
      www.kindlegrove.com
    </p>

    <p class="back-name">Kindle<br>Grove</p>
  </section>

</body>
</html>
```